High profile consultancy

We need a web design for a company called BK Services. BK as abbreviation for Bold Keystone.

Company focusses on Sourcing (BK Sourcing, focus on ICT), Metrics (BK Metrics; focus on business case analysis and trends in ICT) and Software (BK software; to be developed later on; mainly tools supporting BK soucing and metrics)

Customers base consists of large enterprises, >1000 employees.

Site needs to have menu's for
- services
- login
- about
and a special area ' inspire ' to be able to communicate topics that should inspire our customers to contact us.

but key; it schould communicate our expertise and focus on deep knowlegde of ICT sourcing

Reason: please advice on content management systems to be used to maintain site also please advice on Trovix search clickbids. Will provide feedback on designs shortly.

Target Market(s)

CIO's; board of directors;
company excels in ICT / business knowledge and ability to execute; creates / optimizes relations between ICT suppliers and enterprises.

Requirements
Must have
• website should be easily be found; adaptive by design; accessible by all browsers.
• Need to have a login section for later use
Nice to have
• usage of (draft) logo. see upload.

```html
<!DOCTYPE html>
<html lang="en">
<head>
<meta charset="utf-8">
<title>BK Services</title>
<link rel="stylesheet" href="https://fonts.googleapis.com/css2?family=Source+Sans+3:ital,wght@0,300;0,400;0,600;1,300;1,400&display=swap">
<style>
:root{
  --navy:#142347;
  --ink:#1b2a52;
  --sky:#3d9ad8;
  --card-title:#3b8fc6;
  --muted:#8a8f98;
  --body:#3c4250;
  --rule:#dcdfe4;
  --hero-top:#2a3a5c;
  --hero-bottom:#101a33;
  --foot-top:#1f6db0;
  --foot-bottom:#0a3a82;
  --foot-text:#d6e6f7;
  --white:#ffffff;
}
*{box-sizing:border-box;margin:0;padding:0}
html,body{width:875px;height:1200px;overflow:hidden;background:var(--white)}
body{position:relative;font-family:"Source Sans 3",Arial,sans-serif;color:var(--body)}
.abs{position:absolute}

/* header */
.site-header{position:absolute;left:0;top:0;width:875px;height:97px;background:linear-gradient(#ffffff 60%,#eef0f3)}
.brand{left:64px;top:22px;display:flex;align-items:center;gap:10px}
.brand-dot{width:34px;height:34px;border-radius:50%;background:#1f5fae}
.brand-name{font-size:30px;font-weight:400;color:#5a5e66;letter-spacing:.5px}
.login-form{left:468px;top:17px;display:flex;gap:6px}
.login-field{width:82px;height:19px;border:1px solid #c9ccd1;background:#f7f7f7;font-size:9px;color:#8a8f98;padding:3px 6px}
.login-btn{width:41px;height:19px;background:linear-gradient(#2a8ad6,#0f63b0);color:#fff;font-size:9px;text-align:center;line-height:19px;border-radius:2px}
.social{left:715px;top:17px;display:flex;gap:7px}
.social span{width:17px;height:17px;background:#9aa4b3;border-radius:2px}
.main-nav{left:450px;top:62px;display:flex;font-size:14px;color:var(--ink)}
.main-nav a{color:inherit;text-decoration:none;padding:0 14px;border-left:1px solid #c7cad0;line-height:14px}
.main-nav a:first-child{border-left:none;padding-left:0}

/* hero */
.hero{left:0;top:97px;width:875px;height:335px;background:linear-gradient(var(--hero-top),var(--hero-bottom))}
.hero-visual{left:430px;top:3px;width:375px;height:315px;background:radial-gradient(circle at 62% 42%,#3a8fe0 0%,#1c4f96 28%,#12284f 62%,rgba(16,26,51,0) 100%)}
.hero-kicker{left:88px;top:78px;font-size:22px;font-weight:300;color:var(--sky)}
.hero-title{left:88px;top:106px;font-size:29px;font-weight:400;color:var(--white)}
.hero-text{left:93px;top:147px;width:310px;font-size:11.5px;line-height:18px;color:#d3d8e2;font-weight:300}
.hero-dots{left:93px;top:212px;display:flex;gap:4px}
.hero-dots span{width:8px;height:8px;border-radius:50%;background:#5d6b86}
.hero-dots span:first-child{background:#aee0ff}
.arrow{position:absolute}

/* intro */
.intro-title{left:0;width:875px;top:459px;text-align:center;font-size:22px;color:var(--ink)}
.intro-text{left:0;width:875px;top:491px;text-align:center;font-size:11.5px;color:var(--ink)}

/* features */
.feature{top:548px;width:210px;text-align:center}
.feature-visual{width:170px;height:118px;margin:0 auto;border-radius:4px}
.feature-title{margin-top:14px;font-size:16px;color:var(--card-title);font-weight:400}
.feature-text{margin-top:3px;font-size:10px;line-height:16px;color:var(--muted);font-weight:300}
.rule{left:64px;top:782px;width:743px;height:1px;background:var(--rule)}

/* inspire */
.inspire-title{left:0;width:875px;top:802px;text-align:center;font-size:25px;color:var(--ink)}
.quote{display:flex;gap:8px}
.avatar{width:72px;height:72px;border-radius:50%;border:3px solid #eed9d9;flex:none}
.quote-body{font-size:10px;line-height:15px;font-style:italic;font-weight:300;color:var(--body)}
.quote-author{margin-top:6px;font-style:normal;font-weight:400;font-size:10.5px;color:var(--ink)}

/* footer */
.site-footer{left:0;top:981px;width:875px;height:219px;background:linear-gradient(var(--foot-top),var(--foot-bottom))}
.foot-col{top:32px}
.foot-col h3{font-size:15px;font-weight:400;color:var(--white);margin-bottom:5px}
.foot-col li{list-style:none;font-size:10.5px;line-height:18px;color:var(--foot-text);font-weight:300}
.foot-sep{top:30px;width:1px;height:123px;background:rgba(255,255,255,.12)}
.foot-bar{left:4px;top:177px;width:867px;height:1px;background:rgba(255,255,255,.08)}
.copyright{left:65px;top:192px;font-size:9.5px;color:#5f7fb0;font-weight:300}
</style>
</head>
<body>

<header class="site-header">
  <div class="abs brand"><span class="brand-dot"></span><span class="brand-name">BK Services</span></div>
  <form class="abs login-form">
    <div class="login-field">username</div>
    <div class="login-field">password</div>
    <div class="login-btn">Login</div>
  </form>
  <div class="abs social" aria-label="Social links"><span></span><span></span><span></span><span></span></div>
  <nav class="abs main-nav"><a href="#">Home</a><a href="#">Services</a><a href="#">Login</a><a href="#">About</a><a href="#">Contact us</a></nav>
</header>

<section class="abs hero">
  <div class="abs hero-visual" role="img" aria-label="Hand drawing a glowing cloud network diagram linking computers and devices"></div>
  <div class="abs hero-kicker">Business Case Analysis and</div>
  <h1 class="abs hero-title" style="font-weight:400">BK Software Development</h1>
  <p class="abs hero-text">Lorem ipsum dolor sit amet, consectetuer adipiscing elit. Nam cursus. Morbi ut mi. Nullam enim leo, egestas id, condi-mentum at, laoreet mattis, massa.</p>
  <div class="abs hero-dots"><span></span><span></span><span></span><span></span></div>
  <svg class="arrow" style="left:47px;top:128px" width="24" height="56" viewBox="0 0 24 56"><polyline points="22,2 2,28 22,54" fill="none" stroke="#7a86a0" stroke-width="1.5"/></svg>
  <svg class="arrow" style="left:806px;top:128px" width="24" height="56" viewBox="0 0 24 56"><polyline points="2,2 22,28 2,54" fill="none" stroke="#7a86a0" stroke-width="1.5"/></svg>
</section>

<h2 class="abs intro-title" style="font-weight:400">Hasellus felis dolor scelerisque tempus eget lobortis&nbsp; libero</h2>
<p class="abs intro-text">Lorem ipsum dolor sit amet, consectetuer adipiscing elit. Nam cursus. Morbi ut mi. Nullam enim leo, egestas id, condimentum at laoreet</p>

<svg class="arrow" style="left:60px;top:592px" width="12" height="22" viewBox="0 0 12 22"><polyline points="10,1 2,11 10,21" fill="none" stroke="#9aa0a8" stroke-width="1.2"/></svg>
<svg class="arrow" style="left:802px;top:592px" width="12" height="22" viewBox="0 0 12 22"><polyline points="2,1 10,11 2,21" fill="none" stroke="#9aa0a8" stroke-width="1.2"/></svg>

<article class="abs feature" style="left:87px">
  <div class="feature-visual" role="img" aria-label="Tablet showing colourful charts over printed reports" style="background:linear-gradient(135deg,#3a3d44,#c9d3e0 55%,#f2f4f7)"></div>
  <h3 class="feature-title">Duis tincidunt lectus</h3>
  <p class="feature-text">Suspendisse quam leo, molestie sed, luctus quis, feugiat in, pede. Fusce tellus. Sed metus augue, convallis et, vehicula ut</p>
</article>
<article class="abs feature" style="left:330px">
  <div class="feature-visual" role="img" aria-label="Magnifying glass over a blue bar chart report" style="background:linear-gradient(160deg,#e8eef6,#2f7fd0 55%,#dfe6ee)"></div>
  <h3 class="feature-title">Duis tincidunt lectus</h3>
  <p class="feature-text">Suspendisse quam leo, molestie sed, luctus quis, feugiat in, pede. Fusce tellus. Sed metus augue, convallis et, vehicula ut</p>
</article>
<article class="abs feature" style="left:568px">
  <div class="feature-visual" role="img" aria-label="Desktop monitor with website surrounded by app icons" style="background:linear-gradient(180deg,#3a3f48,#6fa8dc 40%,#e9edf2)"></div>
  <h3 class="feature-title">Duis tincidunt lectus</h3>
  <p class="feature-text">Suspendisse quam leo, molestie sed, luctus quis, feugiat in, pede. Fusce tellus. Sed metus augue, convallis et, vehicula ut</p>
</article>

<div class="abs rule"></div>

<h2 class="abs inspire-title" style="font-weight:400">Inspire</h2>

<div class="abs quote" style="left:62px;top:835px">
  <div class="avatar" role="img" aria-label="Portrait of a smiling woman" style="background:radial-gradient(#d9a27a,#8a4a2a)"></div>
  <div class="quote-body" style="width:160px;padding-top:7px">Suspendisse quam leo, molestie sed, luctus quis, feugiat in, pede. Fusce tellus. Sed metus augue, convallis et, vehicula ut, pulvinar eu, ante. Integer orci tellus, tristique vitae
    <div class="quote-author">By Author Name</div></div>
</div>
<div class="abs quote" style="left:324px;top:843px">
  <div class="avatar" role="img" aria-label="Portrait of a smiling older woman" style="background:radial-gradient(#d6b89c,#7a5a40)"></div>
  <div class="quote-body" style="width:165px;padding-top:7px">Morbi eget arcu. Morbi porta, libero id ullamcorper nonummy, nibh ligula pulvinar metus, eget consv et sceleris-que mi tortor at ipsum
    <div class="quote-author">By Author Name</div></div>
</div>
<div class="abs quote" style="left:578px;top:838px">
  <div class="avatar" role="img" aria-label="Portrait of a young man" style="background:radial-gradient(#c9a088,#3a2a24)"></div>
  <div class="quote-body" style="width:160px;padding-top:8px">In massa libero, interdum nec, inter-dum vel, blandit sed, nulla. In ullam-corper, est eget tempor cursus, neque mi consectetuer mi, a ultricies massa est sed nisl.
    <div class="quote-author">By Author Name</div></div>
</div>

<footer class="abs site-footer">
  <div class="abs foot-col" style="left:75px"><h3>Company</h3><ul><li>Cum sociis</li><li>Natoque penatibus</li><li>Magnis dis parturient</li><li>Montes nascetur</li><li>Ridiculus mus</li></ul></div>
  <div class="abs foot-sep" style="left:186px"></div>
  <div class="abs foot-col" style="left:214px"><h3>Services</h3><ul><li>Services Provide</li><li>Natoque penatibus</li><li>Montes nascetur</li><li>Ridiculus mus</li></ul></div>
  <div class="abs foot-sep" style="left:331px"></div>
  <div class="abs foot-col" style="left:353px"><h3>Support</h3><ul><li>Customer Service</li><li>Legal</li><li>Sitemap</li><li>Resources</li></ul></div>
  <div class="abs foot-sep" style="left:449px"></div>
  <div class="abs foot-col" style="left:476px"><h3>Sublinks</h3><ul><li>Services Provide</li><li>Natoque penatibus</li><li>Montes nascetur</li><li>Ridiculus mus</li></ul></div>
  <div class="abs foot-sep" style="left:589px"></div>
  <div class="abs foot-col" style="left:608px"><h3>Sublinks</h3><ul><li>Services Provide</li><li>Natoque penatibus</li><li>Montes nascetur</li><li>Ridiculus mus</li></ul></div>
  <div class="abs foot-bar"></div>
  <p class="abs copyright">© 2013 Company Name.&nbsp; All right reserved.&nbsp; Term of Use</p>
</footer>

</body>
</html>
```